Velliora Events Business Card

We need a business cards that stands out to our clients. We are company who targets prestige clients to spend money with us on experiences, so our image needs to be prestige
Target Market(s)
Corporate
Contact Information for Business Card
There will be four different names on the business cards
Danielle Brontoss
Director
O: 02 5174 2038
M: 0491 652 083
E: info@vellioraevents.example.com.au
Facebook: @vellioraevents
Instagram: vellioraevents
www.vellioraevents.example.com.au
Nathaniel Brontoss
Director
O: 02 5174 2038
M: 0478 205 946
Facebook: @vellioraevents
Instagram: vellioraevents
www.vellioraevents.example.com.au
Elias Dorvek
Director
O: 02 5174 2038
M: 0467 319 752
Facebook: @vellioraevents
Instagram: vellioraevents
www.vellioraevents.example.com.au
Marta Quell
Director
O: 02 5174 2038
Facebook: @vellioraevents
Instagram: vellioraevents
www.vellioraevents.example.com.au
Colors
Designer to choose colors to be used in the design.
Look and feel

```html
<!DOCTYPE html>
<html lang="en">
<head>
<meta charset="utf-8">
<title>Velliora Events — Business Card</title>
<link rel="stylesheet" href="https://fonts.googleapis.com/css2?family=Cinzel:wght@400;500&family=Crimson+Text:wght@400&display=swap">
<style>
  :root {
    --backdrop: #ebe6dc;
    --navy: #242053;
    --navy-deep: #1d1a47;
    --gold: #e8ae4c;
    --gold-light: #f6d58f;
    --gold-pale: #fbf1c4;
    --gold-rich: #f5a623;
    --text-light: #f3ecdc;
  }
  html, body {
    margin: 0;
    padding: 0;
    width: 900px;
    height: 1200px;
    overflow: hidden;
    background: var(--backdrop);
  }
  .canvas {
    position: relative;
    width: 900px;
    height: 1200px;
  }
  .card {
    position: absolute;
    left: 86px;
    width: 734px;
    height: 430px;
    border-radius: 24px;
    overflow: hidden;
  }
  /* Front side */
  .card--front {
    top: 130px;
    background: var(--navy);
  }
  .holder-name {
    position: absolute;
    left: 48px;
    top: 62px;
    margin: 0;
    font-family: "Cinzel", serif;
    font-weight: 500;
    font-size: 27px;
    letter-spacing: 0.5px;
    line-height: 1.1;
    color: var(--gold);
  }
  .holder-role {
    position: absolute;
    left: 48px;
    top: 98px;
    margin: 0;
    font-family: "Crimson Text", serif;
    font-size: 13.5px;
    letter-spacing: 0.3px;
    color: var(--gold);
  }
  .brand {
    position: absolute;
    text-align: center;
    font-family: "Cinzel", serif;
    font-weight: 400;
  }
  .brand__mark {
    display: block;
    margin: 0 auto;
  }
  .brand__name {
    display: block;
    line-height: 1;
  }
  .brand__sub {
    display: block;
    line-height: 1;
  }
  .card--front .brand {
    left: 400px;
    top: 58px;
    width: 324px;
    color: var(--gold);
  }
  .card--front .brand__mark {
    width: 96px;
    height: 96px;
    border-radius: 50%;
    border: 3px solid var(--gold);
    box-sizing: border-box;
    margin-top: 12px;
    margin-bottom: 36px;
  }
  .card--front .brand__name {
    font-size: 34px;
    letter-spacing: 5px;
  }
  .card--front .brand__sub {
    font-size: 18px;
    letter-spacing: 5px;
    margin-top: 10px;
  }
  .divider {
    position: absolute;
    left: 48px;
    top: 287px;
    width: 640px;
    height: 1.5px;
    background: linear-gradient(90deg, var(--text-light), var(--gold-light) 60%, var(--gold));
  }
  .contact-list {
    position: absolute;
    left: 48px;
    top: 298px;
    margin: 0;
    padding: 0;
    list-style: none;
    font-family: "Crimson Text", serif;
    font-size: 15.5px;
    line-height: 23px;
    color: var(--gold-light);
  }
  .contact-list li {
    display: flex;
    align-items: center;
    gap: 10px;
  }
  .contact-list svg {
    width: 15px;
    height: 15px;
    flex: none;
  }
  .address {
    position: absolute;
    right: 46px;
    top: 298px;
    margin: 0;
    font-style: normal;
    text-align: right;
    font-family: "Crimson Text", serif;
    font-size: 15.5px;
    line-height: 23px;
    color: var(--text-light);
  }
  /* Back side */
  .card--back {
    top: 633px;
    background: linear-gradient(118deg,
      var(--gold-pale) 0%,
      var(--gold-rich) 16%,
      var(--gold-pale) 34%,
      #fff7cf 42%,
      var(--gold-rich) 60%,
      #fbd88a 72%,
      var(--gold-rich) 84%,
      var(--gold-pale) 100%);
  }
  .card--back .brand {
    left: 167px;
    top: 100px;
    width: 400px;
    color: var(--navy-deep);
  }
  .card--back .brand__mark {
    width: 110px;
    height: 110px;
    border-radius: 50%;
    background: var(--navy-deep);
    margin-bottom: 50px;
  }
  .card--back .brand__name {
    font-size: 38px;
    letter-spacing: 5px;
  }
  .card--back .brand__sub {
    font-size: 19px;
    letter-spacing: 5px;
    margin-top: 12px;
  }
  .back-url {
    position: absolute;
    left: 0;
    right: 0;
    top: 377px;
    margin: 0;
    text-align: center;
    font-family: "Crimson Text", serif;
    font-size: 15.5px;
    letter-spacing: 1.5px;
    color: var(--navy-deep);
  }
</style>
</head>
<body>
<main class="canvas">

  <section class="card card--front" aria-label="Business card front">
    <h1 class="holder-name">DANIELLE BRONTOSS</h1>
    <p class="holder-role">DIRECTOR</p>

    <div class="brand">
      <span class="brand__mark" aria-hidden="true"></span>
      <span class="brand__name">VELLIORA</span>
      <span class="brand__sub">EVENTS</span>
    </div>

    <div class="divider"></div>

    <ul class="contact-list">
      <li>
        <svg viewBox="0 0 16 16" aria-hidden="true"><path fill="#e8ae4c" d="M3.6 1.5l2.3 2.6-1.2 1.7c.9 2 2.5 3.6 4.5 4.5l1.7-1.2 2.6 2.3-1.4 2.3C7 13.6 2.4 9 1.3 2.9z"/></svg>
        <span>O: 02 5174 2038</span>
      </li>
      <li>
        <svg viewBox="0 0 16 16" aria-hidden="true"><rect x="4" y="1" width="8" height="14" rx="1.5" fill="#e8ae4c"/><rect x="5.5" y="3" width="5" height="8.5" fill="#242053"/><circle cx="8" cy="13.2" r="0.8" fill="#242053"/></svg>
        <span>M: 0491 652 083</span>
      </li>
      <li>
        <svg viewBox="0 0 16 16" aria-hidden="true"><rect x="1" y="3" width="14" height="10" fill="#e8ae4c"/><path d="M1.5 3.5L8 9l6.5-5.5" fill="none" stroke="#242053" stroke-width="1.3"/></svg>
        <span>info@vellioraevents.example.com.au</span>
      </li>
      <li>
        <svg viewBox="0 0 16 16" aria-hidden="true"><g fill="none" stroke="#e8ae4c" stroke-width="1.2"><circle cx="8" cy="8" r="6.4"/><ellipse cx="8" cy="8" rx="2.8" ry="6.4"/><path d="M1.6 8h12.8M2.6 4.8h10.8M2.6 11.2h10.8"/></g></svg>
        <span>www.vellioraevents.example.com.au</span>
      </li>
    </ul>

    <address class="address">
      27 Harwell Street<br>
      Level 4, Sydney<br>
      NSW 2000
    </address>
  </section>

  <section class="card card--back" aria-label="Business card back">
    <div class="brand">
      <span class="brand__mark" aria-hidden="true"></span>
      <span class="brand__name">VELLIORA</span>
      <span class="brand__sub">EVENTS</span>
    </div>
    <p class="back-url">WWW.VELLIORAEVENTS.EXAMPLE.COM.AU</p>
  </section>

</main>
</body>
</html>
```